Business Card Design Project

looking for business cards with new logo

I am looking to keep with the colors of the logo i posted.  Here are some other details to consider.  I would like my website prominently displayed on the business card with the logo.  my website is www.HavenrockTX.com...it should be spelled this way.

My contact information is:

Daniel P Whitcomb III
Broker/Owner
48391 Cordell Ave., Suite 307
Brookvale, Texas 78990
Office: 210-555-0147
Email:  Daniel@HavenrockTX.com

Thank you
Daniel Whitcomb

```html
<!DOCTYPE html>
<html lang="en">
<head>
<meta charset="utf-8">
<title>Havenrock Realty Business Cards</title>
<link rel="stylesheet" href="https://fonts.googleapis.com/css2?family=Open+Sans:wght@400;600&family=Ubuntu:wght@700&family=Arvo:wght@400;700&display=swap">
<style>
  :root {
    --stage: #000000;
    --card-blue: #1f56b8;
    --card-blue-light: #3aa3e0;
    --card-blue-deep: #163f9c;
    --accent-yellow: #f5b700;
    --ribbon-light: #ffe88a;
    --ribbon-dark: #f2b51c;
    --ink: #111111;
    --ink-soft: #333333;
    --white: #ffffff;
  }
  html, body {
    margin: 0;
    width: 1200px;
    height: 1000px;
    overflow: hidden;
    background: var(--stage);
  }
  .stage {
    position: relative;
    width: 1200px;
    height: 1000px;
  }
  .card {
    position: absolute;
    top: 92px;
    width: 417px;
    height: 782px;
    overflow: hidden;
    background: var(--white);
    box-shadow: 0 0 18px rgba(255,255,255,0.6);
  }
  .card--front { left: 152px; }
  .card--back { left: 640px; height: 783px; }
  .card__texture {
    position: absolute;
    left: 0; top: 0;
    width: 100%;
    background: radial-gradient(ellipse 60% 40% at 55% 30%, var(--card-blue-light) 0%, var(--card-blue) 55%, var(--card-blue-deep) 100%);
  }
  .card--front .card__texture { height: 656px; }
  .card--back .card__texture { height: 100%; }

  .ribbon {
    position: absolute;
    left: 28px; top: 78px;
    width: 389px; height: 62px;
  }
  .ribbon__shape { position: absolute; inset: 0; }
  .ribbon__name {
    position: absolute;
    left: 38px; top: 18px;
    font: 700 18px/1.2 "Arvo", serif;
    color: var(--ink);
    white-space: nowrap;
  }
  .ribbon__title {
    position: absolute;
    right: 0; top: 9px;
    width: 112px;
    padding-left: 4px;
    border-left: 1px solid rgba(0,0,0,0.35);
    font: 400 14px/22px "Arvo", serif;
    color: var(--ink);
    text-align: right;
  }
  .ribbon__title span { display: block; }
  .ribbon__title span:first-child { text-align: left; }

  .brand {
    position: absolute;
    left: 0; width: 100%;
    text-align: center;
    color: var(--white);
  }
  .card--front .brand { top: 330px; }
  .card--back .brand { top: 306px; }
  .brand__name {
    display: inline-flex;
    align-items: center;
    gap: 12px;
    font: 400 58px/1 "Open Sans", sans-serif;
    letter-spacing: -1px;
  }
  .brand__mark {
    width: 24px; height: 24px;
    background: var(--white);
  }
  .brand__tagline {
    margin-top: 14px;
    display: flex;
    align-items: center;
    justify-content: center;
    gap: 16px;
    font: 400 22px/1 "Open Sans", sans-serif;
    letter-spacing: 10px;
  }
  .brand__tagline::before,
  .brand__tagline::after {
    content: "";
    width: 60px;
    height: 1px;
    background: var(--white);
  }
  .website {
    position: absolute;
    left: 0; width: 100%;
    text-align: center;
    font: 700 33px/1 "Ubuntu", sans-serif;
    color: var(--accent-yellow);
    white-space: nowrap;
  }
  .card--front .website { top: 456px; }
  .card--back .website { top: 430px; font-size: 34px; }

  .contact {
    position: absolute;
    left: 0; top: 676px;
    width: 100%;
    text-align: center;
    font: 400 13.5px/18px "Open Sans", sans-serif;
    color: var(--ink-soft);
  }
  .contact__phone {
    font-size: 20px;
    line-height: 26px;
    color: var(--ink);
  }
</style>
</head>
<body>
<main class="stage">
  <section class="card card--front">
    <div class="card__texture" role="img" aria-label="Blue paving stone texture background"></div>

    <div class="ribbon">
      <svg class="ribbon__shape" width="389" height="62" viewBox="0 0 389 62" aria-hidden="true">
        <defs>
          <linearGradient id="ribbonFill" x1="0" y1="0" x2="0" y2="1">
            <stop offset="0" stop-color="#ffe88a"/>
            <stop offset="1" stop-color="#f2b51c"/>
          </linearGradient>
        </defs>
        <polygon points="0,0 389,0 389,62 0,62 22,31" fill="url(#ribbonFill)"/>
      </svg>
      <div class="ribbon__name">Daniel P Whitcomb III</div>
      <div class="ribbon__title"><span>BROKER &amp;</span><span>OWNER</span></div>
    </div>

    <div class="brand">
      <div class="brand__name"><span class="brand__mark"></span>Havenrock</div>
      <div class="brand__tagline">REALTY</div>
    </div>
    <div class="website">www.HavenrockTX.com</div>

    <div class="contact">
      <div class="contact__phone">+210-555-0147</div>
      <div>Daniel@HavenrockTX.com :: www.HavenrockTX.com</div>
      <div>48391 Cordell Ave., Suite 307</div>
      <div>Brookvale, Texas 78990</div>
    </div>
  </section>

  <section class="card card--back">
    <div class="card__texture" role="img" aria-label="Blue paving stone texture background"></div>
    <div class="brand">
      <div class="brand__name"><span class="brand__mark"></span>Havenrock</div>
      <div class="brand__tagline">REALTY</div>
    </div>
    <div class="website">www.HavenrockTX.com</div>
  </section>
</main>
</body>
</html>
```